Modern Business Card for Industrial Company

We need business cards updated with modern fonts and make it look more technical, sharp and clean. The logo should not be changed, but we are looking for fresh solutions for how other information on the card is laid out in an interesting way. The company provides machinery and services to the ceramic industry and deals with cutting-edge technology. The design should reflect a technologically advanced and modern company that deals with the latest European technologies.

Font styles to use
Sans Serif

Requirements
Must have
• Modern fonts, technical look and feel

```html
<!DOCTYPE html>
<html lang="en">
<head>
<meta charset="utf-8">
<title>Norvik Service – Business Card</title>
<link href="https://fonts.googleapis.com/css2?family=Montserrat:wght@400;500;700;800&display=swap" rel="stylesheet">
<style>
  :root {
    --brand-blue: #0a5595;
    --brand-blue-deep: #064a86;
    --brand-red: #b3232a;
    --steel-grey: #8f9296;
    --ink: #2b2b2b;
    --paper: #ffffff;
    --backdrop: #d6d6d6;
  }
  * { box-sizing: border-box; margin: 0; padding: 0; }
  html, body {
    width: 1200px; height: 900px; overflow: hidden;
    background: var(--backdrop);
    font-family: "Montserrat", sans-serif;
  }
  .stage {
    width: 1200px; height: 900px;
    display: flex; align-items: center; justify-content: center; gap: 50px;
  }
  .card {
    position: relative;
    width: 540px; height: 308px;
    box-shadow: 0 6px 18px rgba(0,0,0,.18);
    overflow: hidden;
  }

  /* Front */
  .card-front { background: var(--paper); }
  .brand-mark {
    position: absolute; left: 40px; top: 38px;
    display: flex; align-items: center; gap: 10px;
  }
  .brand-mark .mark-square {
    width: 14px; height: 14px; background: var(--brand-red);
  }
  .brand-mark .brand-name {
    font-weight: 800; font-size: 26px; letter-spacing: 1px;
    color: var(--brand-blue); text-transform: uppercase;
  }
  .contact-list {
    position: absolute; left: 40px; top: 168px;
    list-style: none; font-size: 13px; color: var(--ink); line-height: 1.35;
  }
  .contact-list li { display: flex; align-items: flex-start; gap: 7px; margin-bottom: 6px; }
  .contact-list svg { flex: none; width: 12px; height: 12px; margin-top: 2px; fill: var(--brand-red); }
  .holder {
    position: absolute; right: 38px; top: 150px; text-align: right;
  }
  .holder-name {
    font-weight: 800; font-size: 19px; color: var(--brand-blue); letter-spacing: .5px;
    text-transform: uppercase;
  }
  .holder-title { font-size: 14px; color: var(--ink); margin-top: 2px; }
  .edge-accent {
    position: absolute; right: 0; top: 150px; width: 12px; height: 44px; background: var(--brand-red);
  }
  .footer-band {
    position: absolute; left: 0; right: 0; bottom: 0; height: 40px;
    background: var(--brand-blue);
  }
  .footer-band svg { position: absolute; left: 262px; top: 0; }
  .footer-band .web {
    position: absolute; right: 34px; top: 11px;
    color: var(--paper); font-size: 14px; letter-spacing: .4px;
  }

  /* Back */
  .card-back {
    background: linear-gradient(135deg, var(--brand-blue) 0%, var(--brand-blue-deep) 100%);
    display: flex; flex-direction: column; align-items: center; justify-content: center;
  }
  .card-back .brand-mark { position: static; }
  .card-back .brand-name { color: var(--paper); font-size: 34px; }
  .card-back .web {
    margin-top: 42px; color: var(--paper); font-weight: 700; font-size: 15px; letter-spacing: .4px;
  }
</style>
</head>
<body>
<main class="stage">
  <section class="card card-front" aria-label="Business card front">
    <div class="brand-mark">
      <span class="mark-square"></span>
      <span class="brand-name">Norvik Service</span>
    </div>

    <ul class="contact-list">
      <li>
        <svg viewBox="0 0 12 12" aria-hidden="true"><path d="M6 0a4 4 0 0 0-4 4c0 3 4 8 4 8s4-5 4-8a4 4 0 0 0-4-4zm0 5.6A1.6 1.6 0 1 1 6 2.4a1.6 1.6 0 0 1 0 3.2z"/></svg>
        <span>418 Kepler Avenue, Suite 200<br>Brookfield, GA 30120</span>
      </li>
      <li>
        <svg viewBox="0 0 12 12" aria-hidden="true"><path d="M2.6 0.6l1.8 2.2-1 1.2c.7 1.5 1.9 2.8 3.5 3.6l1.2-1 2.3 1.7-.9 2.2C5.4 10.4 1.5 6.5 1 1.5z"/></svg>
        <span>555-014-2290</span>
      </li>
      <li>
        <svg viewBox="0 0 12 12" aria-hidden="true"><path d="M0 2h12v8H0zm1.2 1.1v.3L6 6.8l4.8-3.4v-.3zM1.2 4.8v4h9.6v-4L6 8.2z"/></svg>
        <span>mferrante@norvikservice.com</span>
      </li>
    </ul>

    <div class="holder">
      <p class="holder-name">Marco Ferrante</p>
      <p class="holder-title">President</p>
    </div>
    <span class="edge-accent"></span>

    <footer class="footer-band">
      <svg width="50" height="40" viewBox="0 0 50 40" aria-hidden="true">
        <polygon points="16,0 28,0 12,40 0,40" fill="#b3232a"/>
        <polygon points="30,0 38,0 22,40 14,40" fill="#ffffff"/>
      </svg>
      <span class="web">www.norvikservice.com</span>
    </footer>
  </section>

  <section class="card card-back" aria-label="Business card back">
    <div class="brand-mark">
      <span class="brand-name">Norvik Service</span>
    </div>
    <p class="web">www.norvikservice.com</p>
  </section>
</main>
</body>
</html>
```